IT Tradingsystem for car dealers needs Business Card Design

We need a fresh and modern design for our new business cards.

We develop a it-business system for car dealers in Sweden, Norway and on our way down to further countries in Europe, hence the namechange to BrolaTek Europe AB. The site can be found at www.brolatek-example.com. The startpage is also in for an update/modernization soon so don't take to much from here.

We are looking to print double sided, 4-colour cards.

We want to look professional, modern and serious. Open to cooler suggestions, but not too crazy. We need to make a good and serious impression on our potential customers. It needs to reflect our scandinavian design values and layout.

Preferably with the full BrolaTek logo in good size on the back, so the small print on the logo can be read easily.

Text that needs to go on the cards:
-------

Per Oskar Fjellström
Founder

Direct +46 70-512 96 47
Support 08-612 57 394
po.fjellstrom@brolatek-example.com

BrolaTek Europe AB
Box 8617
104 29 Stockholm

Brolatek-example.com
Saljportalen-example.se

--------
Good luck and thanks!

PS. If you need more input or see what our previous cards looked like, don't hesitate to contact me!

Target Market(s)

Decision makers / executives at brand cardealers

Industry/Entity Type

Automotive

Contact Information for Business Card

Normal size

Requirements
Must have
• Full logo
Nice to have
• Base on our orange colors
Should not have
• No fonts with serif, and not too much graphics

```html
<!DOCTYPE html>
<html lang="en">
<head>
<meta charset="utf-8">
<title>BrolaTek Europe AB – Business Card</title>
<link rel="stylesheet" href="https://fonts.googleapis.com/css2?family=Open+Sans:wght@400;600&display=swap">
<style>
  :root {
    --orange: #f07f22;
    --ink: #2a2a2a;
    --charcoal: #2d2d2d;
    --charcoal-dark: #262626;
    --paper: #ffffff;
    --backdrop: #e9e7e4;
    --logo-grey: #5c5c5c;
  }
  * { box-sizing: border-box; margin: 0; padding: 0; }
  html, body {
    width: 1200px; height: 1000px; overflow: hidden;
    background: var(--backdrop);
    font-family: "Open Sans", Arial, sans-serif;
  }
  .canvas { position: relative; width: 1200px; height: 1000px; }

  .card {
    position: absolute; left: 266px; width: 666px; height: 397px;
    box-shadow: 0 6px 18px rgba(0,0,0,.18);
    overflow: hidden;
  }
  .card--front { top: 74px; background: var(--paper); }
  .card--back  { top: 534px; background: var(--charcoal); }

  /* front */
  .brand {
    position: absolute; display: flex; align-items: center; gap: 12px;
  }
  .brand__mark { background: var(--orange); flex: none; }
  .brand__name { font-weight: 600; letter-spacing: -0.5px; line-height: 1; }

  .card--front .brand { left: 32px; top: 172px; }
  .card--front .brand__mark { width: 44px; height: 44px; }
  .card--front .brand__name { font-size: 40px; color: var(--ink); }

  .divider {
    position: absolute; left: 357px; top: 110px; width: 2px; height: 180px;
    background: linear-gradient(to bottom, rgba(240,127,34,0), var(--orange) 30%, var(--orange) 70%, rgba(240,127,34,0));
  }

  .contact { position: absolute; left: 394px; top: 80px; color: var(--ink); }
  .contact__name { color: var(--orange); font-size: 20px; font-weight: 600; line-height: 24px; }
  .contact__role { font-size: 16px; line-height: 24px; }
  .contact__address { font-size: 16px; line-height: 23px; margin-top: 11px; }
  .contact__lines { list-style: none; margin-top: 13px; font-size: 14.5px; line-height: 23px; }
  .contact__lines li { display: flex; align-items: center; gap: 6px; }
  .contact__lines svg { width: 15px; height: 15px; flex: none; fill: var(--orange); }

  .band { position: absolute; bottom: 0; height: 25px; }
  .band--orange { left: 0; width: 358px; background: var(--orange); }
  .band--dark { left: 358px; right: 0; background: var(--charcoal); }

  /* back */
  .card--back .brand { left: 50%; top: 50%; transform: translate(-50%, -50%); gap: 18px; }
  .card--back .brand__mark { width: 78px; height: 78px; }
  .card--back .brand__name { font-size: 72px; color: var(--logo-grey); }
</style>
</head>
<body>
<main class="canvas">

  <section class="card card--front" aria-label="Business card front">
    <div class="brand">
      <span class="brand__mark"></span>
      <span class="brand__name">BrolaTek</span>
    </div>

    <div class="divider"></div>

    <div class="contact">
      <p class="contact__name">Per Oskar Fjellström</p>
      <p class="contact__role">Founder</p>
      <p class="contact__address">BrolaTek Europe AB<br>Box 8617 104 29 Stockholm</p>
      <ul class="contact__lines">
        <li>
          <svg viewBox="0 0 16 16" aria-hidden="true"><path d="M4.5 1h7a1 1 0 0 1 1 1v12a1 1 0 0 1-1 1h-7a1 1 0 0 1-1-1V2a1 1 0 0 1 1-1zm.5 2v9h6V3zm3 9.6a.8.8 0 1 0 0 1.6.8.8 0 0 0 0-1.6z"/></svg>
          +46 70-512 96 47
        </li>
        <li>
          <svg viewBox="0 0 16 16" aria-hidden="true"><path d="M1 5.5C1 3.5 4 2.5 8 2.5s7 1 7 3v1.2h-3.2V5.2C10.6 4.9 9.4 4.8 8 4.8s-2.6.1-3.8.4v1.5H1zM4.5 7.5h7l2 5.5v1H2.5v-1zM8 9a1.6 1.6 0 1 0 0 3.2A1.6 1.6 0 0 0 8 9z"/></svg>
          08-612 57 394
        </li>
        <li>
          <svg viewBox="0 0 16 16" aria-hidden="true"><path d="M1 3.5h14v9H1zm1.2 1.1v.4L8 9l5.8-4v-.4zm0 1.8v4.9h11.6V6.4L8 10.4z"/></svg>
          po.fjellstrom@brolatek-example.com
        </li>
        <li>
          <svg viewBox="0 0 16 16" aria-hidden="true"><path d="M7 1a6 6 0 0 1 6 6h-1.6A4.4 4.4 0 1 0 7 11.4V13A6 6 0 0 1 7 1zm1 6.2 6.5 2.6-2.7 1 2 2.2-1.1 1-2-2.2-1 2.6z"/></svg>
          www.brolatek-example.com
        </li>
        <li>
          <svg viewBox="0 0 16 16" aria-hidden="true"><path d="M7 1a6 6 0 0 1 6 6h-1.6A4.4 4.4 0 1 0 7 11.4V13A6 6 0 0 1 7 1zm1 6.2 6.5 2.6-2.7 1 2 2.2-1.1 1-2-2.2-1 2.6z"/></svg>
          www.Saljportalen-example.se
        </li>
      </ul>
    </div>

    <div class="band band--orange"></div>
    <div class="band band--dark"></div>
  </section>

  <section class="card card--back" aria-label="Business card back">
    <div class="brand">
      <span class="brand__mark"></span>
      <span class="brand__name">BrolaTek</span>
    </div>
  </section>

</main>
</body>
</html>
```